One Pager Fact Sheet Design

I need a couple of headers and footer designed to use for information security fact sheets to give to customers. Similar to the one listed below.

```html
<!DOCTYPE html>
<html lang="en">
<head>
<meta charset="utf-8">
<title>Security Fact Sheet – Header, Inside Page Header and Footer</title>
<link rel="stylesheet" href="https://fonts.googleapis.com/css2?family=Source+Sans+3:ital,wght@0,400;0,600;0,700;1,700&family=Roboto+Condensed:wght@700&display=swap">
<style>
  :root {
    --brand-red: #d90000;
    --brand-red-dark: #6e0000;
    --brand-red-soft: #e85858;
    --ink-grey: #555555;
    --label-grey: #9a9a9a;
    --dash-grey: #a8a8a8;
    --white: #ffffff;
    --photo-deep: #1e1f2e;
    --photo-mid: #4a3a36;
    --photo-glow: #b8863a;
  }
  * { margin: 0; padding: 0; box-sizing: border-box; }
  html, body { width: 1200px; height: 799px; overflow: hidden; background: var(--white); }
  body { font-family: "Source Sans 3", sans-serif; position: relative; }

  .artboard { position: absolute; inset: 0; width: 1200px; height: 799px; }
  .shapes { position: absolute; inset: 0; }

  .text { position: absolute; white-space: nowrap; line-height: 1; }

  /* Header */
  .brand-mark { position: absolute; left: 31px; top: 50px; width: 76px; height: 76px; border-radius: 50%; background: var(--brand-red); }
  .brand-name { left: 124px; top: 62px; font-size: 52px; font-weight: 700; color: var(--brand-red); letter-spacing: -0.5px; }
  .header-title { left: 124px; top: 150px; font-size: 42px; font-weight: 600; color: var(--ink-grey); }

  .tagline-line1 { font-size: 15px; font-weight: 600; color: var(--white); letter-spacing: 0.2px; }
  .tagline-line2 { font-size: 19px; font-weight: 700; font-style: italic; color: var(--white); }
  .header-tagline-1 { left: 970px; top: 139px; }
  .header-tagline-2 { left: 971px; top: 160px; }

  /* Inside page header */
  .inside-tagline-1 { left: 29px; top: 397px; }
  .inside-tagline-2 { left: 29px; top: 418px; }
  .inside-title { right: 26px; top: 397px; font-size: 32px; font-weight: 600; color: var(--white); }

  /* Footer */
  .page-number { right: 50px; top: 576px; font-size: 25px; font-weight: 600; color: var(--brand-red); }
  .footer-contact { top: 637px; font-size: 24px; font-weight: 400; color: var(--brand-red); }
  .contact-phone { left: 97px; }
  .contact-email { left: 533px; }
  .contact-web { left: 933px; }

  /* Section labels */
  .section-label { font-family: "Roboto Condensed", sans-serif; font-weight: 700; font-size: 30px; color: var(--label-grey); letter-spacing: -0.3px; }
  .label-header { left: 47px; top: 262px; }
  .label-inside { left: 43px; top: 484px; }
  .label-footer { left: 43px; top: 718px; }
</style>
</head>
<body>
<main class="artboard">
  <svg class="shapes" width="1200" height="799" viewBox="0 0 1200 799" xmlns="http://www.w3.org/2000/svg">
    <defs>
      <linearGradient id="cityPhoto" x1="0" y1="0" x2="1" y2="1">
        <stop offset="0" stop-color="var(--photo-deep)"/>
        <stop offset="0.45" stop-color="var(--photo-mid)"/>
        <stop offset="0.75" stop-color="var(--photo-glow)"/>
        <stop offset="1" stop-color="var(--photo-deep)"/>
      </linearGradient>
      <linearGradient id="barShade" x1="0" y1="0" x2="0" y2="1">
        <stop offset="0" stop-color="var(--brand-red-dark)"/>
        <stop offset="1" stop-color="var(--brand-red)"/>
      </linearGradient>
      <linearGradient id="dropShadow" x1="0" y1="0" x2="0" y2="1">
        <stop offset="0" stop-color="#000" stop-opacity="0.35"/>
        <stop offset="1" stop-color="#000" stop-opacity="0"/>
      </linearGradient>
    </defs>

    <!-- Header -->
    <g class="header">
      <polygon points="810,0 1200,0 1200,220 876,220" fill="url(#cityPhoto)" role="img" aria-label="Aerial night view of a city with glowing network lines"/>
      <polygon points="720,0 758,0 840,220 794,220" fill="var(--brand-red-soft)"/>
      <polygon points="756,0 812,0 878,220 838,220" fill="var(--brand-red)"/>
      <polygon points="912,134 932,134 950,186 930,186" fill="var(--white)" opacity="0.55"/>
      <rect x="934" y="134" width="266" height="52" fill="var(--brand-red)"/>
      <rect x="0" y="220" width="1180" height="10" fill="url(#dropShadow)"/>
      <rect x="26" y="220" width="1144" height="26" fill="url(#barShade)"/>
      <line x1="178" y1="281" x2="1150" y2="281" stroke="var(--dash-grey)" stroke-width="1.5" stroke-dasharray="8 7"/>
    </g>

    <!-- Inside page header -->
    <g class="inside-header">
      <rect x="0" y="375" width="1200" height="82" fill="var(--brand-red)"/>
      <polygon points="0,375 340,375 315,457 0,457" fill="url(#cityPhoto)" role="img" aria-label="Aerial night view of a city with glowing network lines"/>
      <polygon points="258,389 276,389 259,441 241,441" fill="var(--white)" opacity="0.55"/>
      <polygon points="0,389 258,389 241,441 0,441" fill="var(--brand-red)"/>
      <line x1="372" y1="497" x2="1150" y2="497" stroke="var(--dash-grey)" stroke-width="1.5" stroke-dasharray="8 7"/>
    </g>

    <!-- Footer -->
    <g class="footer">
      <rect x="28" y="615" width="1144" height="4" fill="var(--brand-red)"/>
      <rect x="28" y="678" width="1144" height="4" fill="var(--brand-red)"/>
      <g class="icon-globe" fill="none" stroke="var(--brand-red)" stroke-width="1.8">
        <circle cx="909" cy="650" r="14"/>
        <ellipse cx="909" cy="650" rx="6" ry="14"/>
        <line x1="895" y1="650" x2="923" y2="650"/>
        <path d="M897 642 H921 M897 658 H921"/>
      </g>
      <line x1="178" y1="733" x2="1150" y2="733" stroke="var(--dash-grey)" stroke-width="1.5" stroke-dasharray="8 7"/>
    </g>
  </svg>

  <!-- Header text -->
  <div class="brand-mark" aria-hidden="true"></div>
  <div class="text brand-name">Brightline Networks</div>
  <h1 class="text header-title">Fact Sheet: Security</h1>
  <div class="text tagline-line1 header-tagline-1">KEEPING YOUR BUSINESS</div>
  <div class="text tagline-line2 header-tagline-2">SAFE &amp; PRODUCTIVE</div>
  <div class="text section-label label-header">HEADER</div>

  <!-- Inside page header text -->
  <div class="text tagline-line1 inside-tagline-1">KEEPING YOUR BUSINESS</div>
  <div class="text tagline-line2 inside-tagline-2">SAFE &amp; PRODUCTIVE</div>
  <h2 class="text inside-title">Fact Sheet: Security</h2>
  <div class="text section-label label-inside">INSIDE PAGEHEADER</div>

  <!-- Footer text -->
  <div class="text page-number">Security | Pg 2</div>
  <div class="text footer-contact contact-phone">Contact: Phone: 555-013-0147</div>
  <div class="text footer-contact contact-email">Email: info@brightlinenet.com</div>
  <div class="text footer-contact contact-web">www.brightlinenet.com</div>
  <div class="text section-label label-footer">FOOTER</div>
</main>
</body>
</html>
```